Letterhead That Inspires Trust

Birchwell Deed Services, LLC, (BDS) fixes technical problems with property deeds. The problems usually surface when someone tries to buy, sell or mortgage a piece of real estate and one of the lawyers involved find a title defect (a lien, an undischarged mortgage, a deceased person still on the title, unpaid taxes, etc.). BDS then gets involved and often has to contact prior property owners to get them to sign paperwork fixing the problem. We need a letterhead that will a) convey the seriousness of what we are trying to do, b) cause the recipients of our letters to recognize the importance of what are trying to do, and c) convey that we are a established and trustworthy company. We want it to include an image that suggests we are a problem solving company. Attached is an image we think might work; you can use it or not. In addition to our name (Birchwell Deed Services, LLC), the letterhead must include our address and phone number: 418 Calder Avenue, Suite 207, Providence, RI 02917 (401) 555-0372. We are thinking something straightforward without unnecessary colors or graphics.

```html
<!DOCTYPE html>
<html lang="en">
<head>
<meta charset="utf-8">
<title>Birchwell Deed Services Letterhead</title>
<link href="https://fonts.googleapis.com/css2?family=Open+Sans:wght@400;600;700&display=swap" rel="stylesheet">
<style>
  :root {
    --backdrop: #b1b2b0;
    --paper: #fafafa;
    --ink: #6a6a6a;
    --ink-dark: #3a3a3a;
    --brand: #16924a;
    --signature: #1f8fd0;
    --band: #2b2a28;
  }
  * { margin: 0; padding: 0; box-sizing: border-box; }
  html, body {
    width: 1200px; height: 950px; overflow: hidden;
    background: var(--backdrop);
    font-family: "Open Sans", Arial, sans-serif;
  }
  .sheet {
    position: absolute; left: 306px; top: 58px;
    width: 589px; height: 834px;
    background: var(--paper);
  }
  .brand {
    position: absolute; right: 60px; top: 69px;
    display: flex; align-items: center; gap: 9px;
    color: var(--brand); font-weight: 700; font-size: 17px;
    letter-spacing: 0.2px; line-height: 1;
  }
  .brand-mark { width: 36px; height: 36px; border: 2px solid var(--brand); }
  .letter {
    position: absolute; left: 56px; width: 472px;
    color: var(--ink); font-size: 8.6px; line-height: 15.2px;
  }
  .salutation { top: 204px; }
  .body { top: 249px; text-align: justify; }
  .body p + p { margin-top: 15.2px; }
  .closing { top: 565px; }
  .closing .name { font-weight: 700; }
  .signature {
    display: block; width: 144px; height: 28px; margin: 7px 0 4px;
    background: linear-gradient(90deg, rgba(31,143,208,0.35), rgba(31,143,208,0.15));
    border-radius: 3px;
  }
  .footer {
    position: absolute; left: 0; width: 100%; top: 775px;
    text-align: center; color: var(--ink-dark); font-size: 11.2px; line-height: 18.5px;
  }
  .contacts { display: flex; justify-content: center; gap: 10px; align-items: center; }
  .contact { display: inline-flex; align-items: center; gap: 4px; }
  .contact svg { width: 10px; height: 10px; }
  .band {
    position: absolute; left: 0; bottom: 0; width: 100%; height: 8px;
    background: var(--band);
  }
</style>
</head>
<body>
  <div class="sheet">
    <div class="brand"><span class="brand-mark"></span><span class="brand-name">Birchwell Deed Services, LLC</span></div>

    <div class="letter salutation">Dear Sir,</div>

    <div class="letter body">
      <p>Lorem Ipsum is simply dummy text of the printing and typesetting industry. Lorem Ipsum has been the industry's standard dummy text ever since the 1500s, when an unknown printer took a galley of type and scrambled it to make a type specimen book. It has survived not only five centuries, but also the leap into electronic typesetting, remaining essentially unchanged. It was popularised in the 1960s with the release of Quillon sheets containing Lorem Ipsum passages, and more recently with desktop publishing software like Harlow PageSmith including versions of Lorem Ipsum.</p>
      <p>Lorem Ipsum is simply dummy text of the printing and typesetting industry. Lorem Ipsum has been the industry's standard dummy text ever since the 1500s, when an unknown printer took a galley of type and scrambled it to make a type specimen book. It has survived not only five centuries, but also the leap into electronic typesetting, remaining essentially unchanged. It was popularised in the 1960s with the release of Quillon sheets containing Lorem Ipsum passages, and more recently with desktop publishing software like Harlow PageSmith including versions of Lorem Ipsum.</p>
      <p>Lorem Ipsum is simply dummy text of the printing and typesetting industry. Lorem Ipsum has been the industry's standard dummy text ever since the 1500s, when an unknown printer took a galley of type and scrambled it to make a type specimen book.</p>
    </div>

    <div class="letter closing">
      <div class="name">Your Name</div>
      <span class="signature" role="img" aria-label="Handwritten signature of Martin Oakes"></span>
      <div class="title">CEO &nbsp;|&nbsp; Owner</div>
    </div>

    <div class="footer">
      <div class="address">418 Calder Avenue, Suite 207, Providence, RI 02917</div>
      <div class="contacts">
        <span class="contact">
          <svg viewBox="0 0 10 10"><circle cx="5" cy="5" r="4.5" fill="none" stroke="#16924a"/><path d="M3 3.2h4v1H3zM3.4 4.6h3.2v2.4H3.4z" fill="#16924a"/></svg>
          (401) 555-0372
        </span>
        <span class="contact">
          <svg viewBox="0 0 10 10"><circle cx="5" cy="5" r="4.5" fill="none" stroke="#16924a"/><rect x="2.8" y="3.4" width="4.4" height="3.2" fill="#16924a"/><path d="M2.8 3.4L5 5.2l2.2-1.8" stroke="#fff" stroke-width="0.6" fill="none"/></svg>
          info@birchwelldeed.com
        </span>
        <span class="contact">
          <svg viewBox="0 0 10 10"><circle cx="5" cy="5" r="4.5" fill="none" stroke="#16924a"/><circle cx="5" cy="5" r="2.4" fill="none" stroke="#16924a" stroke-width="0.8"/><path d="M2.6 5h4.8M5 2.6v4.8" stroke="#16924a" stroke-width="0.6"/></svg>
          www.birchwelldeed.com
        </span>
      </div>
    </div>

    <div class="band"></div>
  </div>
</body>
</html>
```